Letterhead Design Project

Professional but modern letterhead.

Target Market(s)

mining companies

Industry/Entity Type

It Professional

Colors

Designer to choose colors to be used in the design.

```html
<!DOCTYPE html>
<html lang="en">
<head>
<meta charset="utf-8">
<title>KORA Letterhead</title>
<link href="https://fonts.googleapis.com/css2?family=Questrial&display=swap" rel="stylesheet">
<style>
  :root {
    --brand-blue: #2a5391;
    --paper: #ffffff;
    --rule-grey: #8a8a8a;
    --tint-lilac: #e0dff0;
    --text-light: #ffffff;
  }
  html, body {
    margin: 0;
    padding: 0;
    overflow: hidden;
    background: var(--paper);
  }
  .letterhead {
    position: relative;
    width: 831px;
    height: 1200px;
    overflow: hidden;
    background: var(--paper);
    font-family: "Questrial", "Century Gothic", sans-serif;
  }
  .top-rule {
    position: absolute;
    left: 0; top: 0;
    width: 100%;
    height: 2px;
    background: var(--rule-grey);
  }
  .contact-band {
    position: absolute;
    left: 0; top: 33px;
    width: 571px;
    height: 88px;
    background: var(--brand-blue);
    color: var(--text-light);
    font-size: 13px;
    line-height: 19px;
  }
  .contact-col {
    position: absolute;
    top: 6px;
    white-space: nowrap;
  }
  .contact-col p { margin: 0; }
  .contact-col--address { left: 20px; }
  .contact-col--online { left: 175px; }
  .brand-mark {
    position: absolute;
    left: 578px; top: 34px;
    width: 68px;
    display: flex;
    flex-direction: column;
    align-items: center;
    gap: 6px;
    color: var(--brand-blue);
  }
  .brand-mark__dot {
    width: 44px; height: 44px;
    border-radius: 50%;
    background: var(--brand-blue);
  }
  .brand-mark__name {
    font-size: 28px;
    line-height: 1;
    letter-spacing: 0.5px;
  }
  .backdrop-accent {
    position: absolute;
    left: 0; top: 0;
  }
  .footer-band {
    position: absolute;
    left: 0; bottom: 0;
    width: 100%;
    height: 109px;
    background: var(--brand-blue);
  }
</style>
</head>
<body>
  <div class="letterhead">
    <div class="top-rule"></div>

    <svg class="backdrop-accent" width="831" height="1200" aria-hidden="true">
      <circle cx="890" cy="800" r="226" fill="var(--tint-lilac)"/>
    </svg>

    <header class="contact-band">
      <div class="contact-col contact-col--address">
        <p>48 Ridgeway Avenue</p>
        <p>Harlow Park, Unit 7</p>
        <p>Tel &nbsp;: &nbsp;+044 218 5570</p>
        <p>Fax : +044 218 5571</p>
      </div>
      <div class="contact-col contact-col--online">
        <p>Email :</p>
        <p>info@kora.com</p>
        <p>Website :</p>
        <p>www.kora.com</p>
      </div>
    </header>

    <div class="brand-mark">
      <span class="brand-mark__dot"></span>
      <span class="brand-mark__name">KORA</span>
    </div>

    <footer class="footer-band"></footer>
  </div>
</body>
</html>
```